Home Page Website Design

The Site width is 1000 px. I've attached a Balsamiq mockup as a design layout guide. The design needs to be flat and clean. Please stick to the pixel dimensions of the mock up as the site will be responsive. I've also attached the logos used on the mockup for positional purposes.

Colours to use: Black, Grey, Green (Logo tie in) & green complementary colours.

Green (Logo tie in)
White Background
Titles: Black (Roboto Bold 700)
Text: Dark Grey (Roboto Normal 400)

Look & Style Example
http://www.brindlowlearn.org.uk/

Type Face
Google Fonts - Roboto

These are just guidelines, please feel free to use you own creative judgment.

Thanks

```html
<!DOCTYPE html>
<html lang="en">
<head>
<meta charset="utf-8">
<title>Brindlow Teaching School Alliance – Home</title>
<link rel="stylesheet" href="https://fonts.googleapis.com/css2?family=Roboto:wght@400;700&family=Questrial&display=swap">
<style>
:root{
  --green:#22bf62;
  --green-dark:#12a24c;
  --yellow:#f6d11a;
  --black:#111;
  --nav:#222;
  --grey-dark:#555;
  --grey-panel:#e6e6e6;
  --grey-btn:#dcdcdc;
  --text:#333;
  --line:#888;
  --white:#fff;
}
*{box-sizing:border-box;margin:0;padding:0}
html,body{width:893px;height:1200px;overflow:hidden;background:var(--white)}
body{position:relative;font-family:Roboto,Arial,sans-serif;color:var(--text)}
.abs{position:absolute}
.heading{font-family:Questrial,Arial,sans-serif;font-weight:400;color:var(--black)}

/* header */
.brand{left:6px;top:10px;width:160px}
.brand-mark{font-family:Questrial,sans-serif;font-size:50px;color:var(--green);letter-spacing:2px;line-height:60px;padding-left:30px}
.brand-name{font-size:9px;color:var(--green);margin-top:8px}
.login{left:823px;top:3px;width:66px;height:20px;background:var(--green);color:var(--white);font-family:Questrial,sans-serif;font-size:12px;text-align:center;line-height:20px}
.live-chat{left:530px;top:24px;width:56px;text-align:center;font-size:10px;font-weight:700;color:var(--grey-dark)}
.register{left:605px;top:25px;width:284px;height:61px;background:var(--grey-dark)}
.register h2{position:absolute;left:15px;top:6px;font-size:18px;color:var(--white)}
.register .email{position:absolute;left:12px;top:30px;width:172px;height:22px;background:var(--white);font-size:12px;line-height:22px;padding-left:8px;color:var(--black)}
.register .submit{position:absolute;left:196px;top:30px;width:75px;height:22px;background:#c8c8c8;font-size:12px;line-height:22px;text-align:center;color:var(--black)}

/* nav */
.nav{left:3px;top:98px;width:887px;height:33px;background:var(--nav);display:flex;align-items:center}
.nav a{color:var(--white);text-decoration:none;font-size:11px;margin-left:18px;margin-right:5px}
.nav a:first-child{margin-left:19px}
.search{left:681px;top:104px;width:203px;height:22px;background:var(--white);font-size:11px;line-height:22px;padding-left:9px;color:var(--black)}
.search svg{position:absolute;right:5px;top:3px}

/* hero */
.hero-photo{left:3px;top:131px;width:887px;height:299px;background:linear-gradient(100deg,#d8d6d2 0%,#c9c3bb 35%,#e8e6e3 55%,#b9b1a8 75%,#dcdcdc 100%)}
.hero-panel{left:12px;top:143px;width:343px;height:278px;background:var(--green);color:var(--white)}
.hero-panel h1{position:absolute;left:17px;top:15px;font-size:25px;color:var(--white);white-space:nowrap}
.hero-panel p{position:absolute;left:18px;top:68px;width:312px;font-size:11.5px;line-height:14px}
.hero-btn{position:absolute;left:18px;top:201px;width:105px;height:28px;background:var(--yellow);color:var(--black);font-size:11.5px;line-height:28px;text-align:center}

/* sections */
.section-title{font-size:21.5px;top:450px}
.panel{background:var(--grey-panel)}
.welcome{left:4px;top:482px;width:284px;height:415px}
.video{position:absolute;left:11px;top:10px;width:263px;height:164px;background:#000}
.video .bar{position:absolute;left:0;bottom:0;width:100%;height:18px;background:#1a1a1a;color:#bbb;font-size:6px;line-height:18px;padding-left:50px}
.video .track{position:absolute;left:4px;bottom:18px;width:255px;height:2px;background:#444}
.welcome p{position:absolute;left:13px;top:196px;width:262px;font-size:10.7px;line-height:12.9px;color:var(--black)}

.training{left:305px;top:482px;width:284px;height:191px;border:1px solid var(--line)}
.training ul{list-style:none;position:absolute;left:13px;top:13px}
.training li{width:258px;height:28px;margin-bottom:5px;background:var(--grey-btn);border:1px solid #c9c9c9;font-size:11.5px;color:var(--black);line-height:26px;padding-left:11px;position:relative}
.training li svg{position:absolute;right:9px;top:7px}

.news{left:305px;top:714px;width:284px;height:183px;border:1px solid var(--line)}
.news article{position:absolute;left:17px;width:258px}
.news h3{font-weight:400;font-size:15.5px;color:var(--black);margin-bottom:4px}
.news p{font-size:9.6px;line-height:12.5px;color:#555}

.courses{left:605px;top:482px;width:284px;height:415px}
.course{position:absolute;left:17px;width:248px}
.course h3{font-size:14px;line-height:14px;color:var(--black)}
.course p{font-size:10px;line-height:14px;color:#444;margin-top:8px}
.course .foot{display:flex;align-items:center;margin-top:8px}
.course .places{font-size:12px;color:var(--green)}
.course .book{margin-left:16px;width:55px;height:22px;background:var(--grey-dark);color:var(--white);font-size:12px;text-align:center;line-height:22px}
.course-rule{position:absolute;left:17px;width:248px;height:1px;background:#999}
.pager{left:822px;top:869px}

/* footer */
.footer-col{top:932px;font-size:11.5px;line-height:13.8px;color:var(--black)}
.partner-net{left:720px;top:932px;display:flex;align-items:center;gap:6px;font-size:11.5px;color:var(--black)}
.partner-net .dot{width:14px;height:14px;border-radius:50%;background:var(--green)}
.social{top:942px;width:25px;height:25px;border-radius:50%;background:#bdbdbd}

.partners{left:0;top:1055px;width:893px;height:80px}
.partner-bar{left:20px;top:1132px;width:853px;height:7px;background:var(--grey-dark);box-shadow:0 6px 8px -4px rgba(0,0,0,.35)}
.copyright{left:0;top:1166px;width:893px;text-align:center;font-size:10.7px;color:var(--black)}
</style>
</head>
<body>

<header>
  <div class="abs brand">
    <div class="brand-mark">BTA</div>
    <div class="brand-name">Brindlow Teaching School Alliance</div>
  </div>
  <div class="abs login">Login</div>
  <div class="abs live-chat">
    <svg width="46" height="52" viewBox="0 0 46 52" aria-hidden="true">
      <circle cx="23" cy="17" r="11" fill="#444"/>
      <path d="M4 52 C4 36 12 31 23 31 C34 31 42 36 42 52Z" fill="#444"/>
      <path d="M10 18 C10 4 36 4 36 18" fill="none" stroke="#444" stroke-width="3"/>
    </svg>
    <div>Live Chat</div>
  </div>
  <div class="abs register">
    <h2 class="heading" style="color:#fff">Register Now</h2>
    <div class="email">email address</div>
    <div class="submit">Submit</div>
  </div>
</header>

<nav class="abs nav">
  <a href="#">Home</a><a href="#">About Us</a><a href="#">Training &amp; Development</a><a href="#">Benefits</a><a href="#">Members</a><a href="#">What's On</a><a href="#">Contact us</a><a href="#">News</a><a href="#">Forum</a>
</nav>
<div class="abs search">search
  <svg width="16" height="16" viewBox="0 0 16 16" aria-hidden="true"><circle cx="6.5" cy="6.5" r="5" fill="none" stroke="#111" stroke-width="2"/><path d="M10 10 L15 15" stroke="#111" stroke-width="2.5"/></svg>
</div>

<section>
  <div class="abs hero-photo" role="img" aria-label="Photo of teachers gathered around a tablet in a workshop"></div>
  <div class="abs hero-panel">
    <h1 class="heading" style="color:#fff">New Teachers in Workshop</h1>
    <p>Lorem ipsum dolor sit amet, consectetur adipisicing elit, sed do eiusmod tempor incididunt ut labore et dolore magna aliqua. Ut enim ad minim veniam, quis nostrud exercitation ullamco laboris nisi ut aliquip ex ea commodo consequat. Duis aute irure dolor in reprehenderit in voluptate velit esse cillum dolore eu fugiat nulla pariatur. Excepteur sint occaecat cupidatat non proident, sunt in culpa qui officia deserunt mollit anim id est laborum.</p>
    <div class="hero-btn">Find Our More</div>
  </div>
</section>

<h2 class="abs heading section-title" style="left:7px">Welcome</h2>
<h2 class="abs heading section-title" style="left:307px">Training &amp; Development</h2>
<h2 class="abs heading section-title" style="left:605px">Latest Courses</h2>

<section class="abs panel welcome">
  <div class="video">
    <div class="track"></div>
    <div class="bar">00:00 / 18:50</div>
  </div>
  <p>Sed ut perspiciatis, unde omnis iste natus error sit voluptatem accusantium doloremque laudantium, totam rem aperiam eaque ipsa, quae ab illo inventore veritatis et quasi architecto beatae vitae dicta sunt, explicabo. Nemo enim ipsam voluptatem, quia voluptas sit, aspernatur aut odit aut fugit, sed quia consequuntur magni dolores eos, qui ratione voluptatem sequi nesciunt, neque porro quisquam est, qui dolorem ipsum, quia dolor sit amet, consectetur, adipisci[ng] velit, sed quia non numquam [do] eius modi tempora inci[di]dunt, ut labore et dolore magnam aliquam quaerat voluptatem. Ut enim ad minima veniam, quis nostrum exercitationem ullam corporis suscipit laboriosam, nisi ut aliquid ex ea commodi consequatur?</p>
</section>

<section class="abs training">
  <ul>
    <li>Leadership Training<svg width="12" height="13" viewBox="0 0 12 13" aria-hidden="true"><path d="M0 0 L12 6.5 L0 13Z" fill="#000"/></svg></li>
    <li>CPD<svg width="12" height="13" viewBox="0 0 12 13" aria-hidden="true"><path d="M0 0 L12 6.5 L0 13Z" fill="#000"/></svg></li>
    <li>School 2 School Support<svg width="12" height="13" viewBox="0 0 12 13" aria-hidden="true"><path d="M0 0 L12 6.5 L0 13Z" fill="#000"/></svg></li>
    <li>Research &amp; Development<svg width="12" height="13" viewBox="0 0 12 13" aria-hidden="true"><path d="M0 0 L12 6.5 L0 13Z" fill="#000"/></svg></li>
    <li>IT (School Direct)<svg width="12" height="13" viewBox="0 0 12 13" aria-hidden="true"><path d="M0 0 L12 6.5 L0 13Z" fill="#000"/></svg></li>
  </ul>
</section>

<h2 class="abs heading section-title" style="left:307px;top:688px">News</h2>
<section class="abs news">
  <article style="top:22px">
    <h3>Lorem ipsum dolor sit amet</h3>
    <p>At vero eos et accusamus et iusto odio dignissimos ducimus, qui blanditiis praesentium voluptatum deleniti atque corrupti, quos dolores et quas molestias excepturi</p>
  </article>
  <article style="top:100px">
    <h3>Lorem ipsum dolor sit amet</h3>
    <p>At vero eos et accusamus et iusto odio dignissimos ducimus, qui blanditiis praesentium voluptatum deleniti atque corrupti, quos dolores et quas molestias excepturi</p>
  </article>
</section>

<section class="abs panel courses">
  <div class="course" style="top:20px">
    <h3>Want to deliver consistently ‘Outstanding Lessons?’</h3>
    <p>Nam libero tempore, cum soluta nobis est eligendi optio, cumque nihil impedit, quo minus id, quod</p>
    <div class="foot"><span class="places">6 places left</span><span class="book">Book</span></div>
  </div>
  <div class="course-rule" style="top:129px"></div>
  <div class="course" style="top:147px">
    <h3>Want to deliver consistently ‘Outstanding Lessons?’</h3>
    <p>Nam libero tempore, cum soluta nobis est eligendi optio, cumque nihil impedit, quo minus id, quod</p>
    <div class="foot"><span class="places">6 places left</span><span class="book">Book</span></div>
  </div>
  <div class="course-rule" style="top:255px"></div>
  <div class="course" style="top:272px">
    <h3>Want to deliver consistently ‘Outstanding Lessons?’</h3>
    <p>Nam libero tempore, cum soluta nobis est eligendi optio, cumque nihil impedit, quo minus id, quod</p>
    <div class="foot"><span class="places">6 places left</span><span class="book">Book</span></div>
  </div>
</section>
<svg class="abs pager" width="50" height="22" viewBox="0 0 50 22" aria-hidden="true">
  <circle cx="10" cy="11" r="10" fill="var(--green-dark)"/><path d="M13 6 L6 11 L13 16Z" fill="#fff"/>
  <circle cx="39" cy="11" r="10" fill="var(--green-dark)"/><path d="M36 6 L43 11 L36 16Z" fill="#fff"/>
</svg>

<footer>
  <div class="abs footer-col" style="left:15px">Brindlow Teaching Schools Alliance<br>Marlow Lane<br>Ashbridge<br>AB4 2QT<br>Tel: 01632 960418<br>email:info@brindlowteaching.org.uk</div>
  <div class="abs footer-col" style="left:331px">About Us<br>Training &amp; Development<br>Benefits<br>Members<br>Calendar Events</div>
  <div class="abs footer-col" style="left:511px">Contact Us<br>News<br>Forum<br>Site Map</div>
  <div class="abs partner-net"><span class="dot"></span><span>Fernvale<br>Schools<br>Network</span></div>
  <div class="abs social" style="left:812px"></div>
  <div class="abs social" style="left:845px"></div>

  <svg class="abs partners" width="893" height="80" viewBox="0 0 893 80" aria-label="Partner schools and universities">
    <path d="M62 12 L42 40 L62 68 L52 68 L32 40 L52 12Z" fill="#555"/>
    <path d="M830 12 L850 40 L830 68 L840 68 L860 40 L840 12Z" fill="#555"/>
    <rect x="96" y="10" width="46" height="58" rx="6" fill="#8a6a4a"/>
    <rect x="176" y="10" width="40" height="58" rx="4" fill="#2f8f4a"/>
    <rect x="245" y="8" width="62" height="64" rx="3" fill="#1d2f8f"/>
    <circle cx="368" cy="38" r="28" fill="#2a4aa0"/>
    <rect x="423" y="18" width="90" height="40" rx="4" fill="#c9c9c9"/>
    <circle cx="567" cy="38" r="30" fill="#1b3a7a"/>
    <rect x="630" y="8" width="46" height="62" rx="10" fill="#3a5a8f"/>
    <circle cx="748" cy="40" r="32" fill="#ee5a2a"/>
  </svg>
  <div class="abs partner-bar"></div>
  <div class="abs copyright">© Copyright&nbsp; Brindlow Teaching Schools Alliance</div>
</footer>

</body>
</html>
```